Crestline Gas and Plumbing Business Card Design

I am after a business card design for my plumbing business called 'Crestline Gas & Plumbing'. I do all types of plumbing and gas work and specialise in general maintenance plumbing. Would like to see designs using current logo

Industry/Entity Type

Plumbing

Contact Information for Business Card

Name - Dale Whitcombe
Phone number - 0455163027
Email - admin@crestlinegasandplumbing.example.com.au
ABN - 68204915336

```html
<!DOCTYPE html>
<html lang="en">
<head>
<meta charset="utf-8">
<title>Crestline Gas &amp; Plumbing — Business Cards</title>
<link rel="stylesheet" href="https://fonts.googleapis.com/css2?family=Open+Sans:wght@400;600;700&display=swap">
<style>
  :root {
    --bg: #2a2c30;
    --card-white: #ffffff;
    --card-black: #0b0b0c;
    --brand-blue: #2b46b8;
    --brand-blue-light: #3a7fd6;
    --brand-yellow: #ffc21a;
    --brand-orange: #f5922a;
    --brand-red: #ea5a2a;
    --ink-dark: #1d1d1f;
    --ink-light: #f2f2f2;
  }
  * { margin: 0; padding: 0; box-sizing: border-box; }
  html, body { width: 1200px; height: 900px; overflow: hidden; }
  body {
    background: var(--bg);
    font-family: "Open Sans", Arial, sans-serif;
    position: relative;
  }
  .card {
    position: absolute;
    left: 340px;
    width: 520px;
    height: 300px;
    border-radius: 22px;
    overflow: hidden;
  }

  /* Front */
  .card-front {
    top: 100px;
    background: var(--card-white);
  }
  .front-band-top {
    position: absolute; left: 0; right: 0; top: 0; height: 12px;
    background: linear-gradient(90deg, var(--brand-yellow), var(--brand-orange) 60%, var(--brand-red));
  }
  .front-band-bottom {
    position: absolute; left: 0; right: 0; bottom: 0; height: 12px;
    background: linear-gradient(90deg, var(--brand-blue), var(--brand-blue-light) 50%, var(--brand-blue));
  }
  .front-brand {
    position: absolute; left: 0; right: 0; top: 108px;
    display: flex; align-items: center; justify-content: center; gap: 14px;
  }
  .brand-mark {
    width: 34px; height: 34px; border-radius: 50%;
    background: var(--brand-orange);
  }
  .brand-name {
    font-size: 30px; font-weight: 700; color: var(--brand-blue);
    letter-spacing: 0.5px;
  }
  .front-web {
    position: absolute; left: 0; right: 0; top: 200px;
    text-align: center; font-size: 15px; color: var(--ink-dark);
  }

  /* Back */
  .card-back {
    top: 500px;
    background: var(--card-black);
    color: var(--ink-light);
  }
  .holder-name {
    position: absolute; left: 0; right: 0; top: 34px;
    text-align: center; font-size: 32px; font-weight: 700;
    color: var(--brand-orange);
  }
  .divider {
    position: absolute; left: 40px; right: 40px; top: 128px;
    display: flex; align-items: center; gap: 16px;
  }
  .divider-line { flex: 1; height: 1.5px; background: var(--brand-orange); }
  .divider-mark {
    width: 40px; height: 40px; border-radius: 50%;
    background: var(--brand-orange);
  }
  .contact {
    position: absolute; left: 0; right: 0; top: 180px;
    text-align: center; list-style: none; font-size: 16px; line-height: 1.65;
  }
  .contact-email { color: var(--brand-orange); }
</style>
</head>
<body>

  <section class="card card-front" aria-label="Business card front">
    <div class="front-band-top"></div>
    <div class="front-brand">
      <span class="brand-mark"></span>
      <span class="brand-name">Crestline Gas &amp; Plumbing</span>
    </div>
    <p class="front-web">www.crestlinegasandplumbing.example.com.au</p>
    <div class="front-band-bottom"></div>
  </section>

  <section class="card card-back" aria-label="Business card back">
    <h1 class="holder-name">Dale Whitcombe</h1>
    <div class="divider">
      <span class="divider-line"></span>
      <span class="divider-mark"></span>
      <span class="divider-line"></span>
    </div>
    <ul class="contact">
      <li class="contact-phone">0455163027</li>
      <li class="contact-email">admin@crestlinegasandplumbing.example.com.au</li>
      <li class="contact-abn">ABN - 68204915336</li>
    </ul>
  </section>

</body>
</html>
```